Business Card Designs

Looking to design a 3.5" x 2" standard business card for our employees.
The design needs to be sleek, simple, and modern. We would like our logo (attached) to be incorporated, but not in that colour, rather an outline of the logo in either gold or silver (whichever looks better).

Modern and Simple is what we are looking for, but be creative in incorporating the logo.

```html
<!DOCTYPE html>
<html lang="en">
<head>
<meta charset="utf-8">
<title>Harbourline Suites – Business Card</title>
<link rel="stylesheet" href="https://fonts.googleapis.com/css2?family=Lato:wght@400;700;900&display=swap">
<style>
  :root {
    --backdrop: #e9e9e9;
    --card: #262626;
    --card-pattern: #2c2c2c;
    --gold: #c9a13b;
    --ink-light: #e8e8e8;
    --rule: #8a8a8a;
  }
  * { box-sizing: border-box; margin: 0; padding: 0; }
  html, body { width: 1200px; height: 802px; overflow: hidden; }
  body {
    background: var(--backdrop);
    font-family: "Lato", Arial, sans-serif;
    position: relative;
  }
  .card {
    position: absolute;
    width: 520px;
    height: 297px;
    background: var(--card);
    border-radius: 3px;
    box-shadow: 0 6px 18px rgba(0,0,0,0.18);
    overflow: hidden;
  }
  .card--front { left: 60px; top: 120px; }
  .card--back { left: 620px; top: 385px; }

  .brand {
    display: flex;
    flex-direction: column;
    align-items: center;
    color: var(--gold);
    font-weight: 900;
  }
  .brand__name {
    display: flex;
    align-items: center;
    gap: 8px;
    font-size: 19px;
    letter-spacing: 2px;
  }
  .brand__square {
    width: 12px; height: 12px;
    background: var(--gold);
  }
  .brand__sub {
    font-size: 10px;
    letter-spacing: 4px;
    margin-top: 4px;
  }

  .card--front .brand {
    position: absolute;
    left: 20px; top: 0; bottom: 0;
    width: 230px;
    justify-content: center;
  }
  .divider {
    position: absolute;
    left: 262px; top: 70px;
    width: 1px; height: 157px;
    background: var(--rule);
  }
  .contact {
    position: absolute;
    left: 284px; top: 66px;
    color: var(--ink-light);
    font-size: 13px;
    line-height: 1.5;
  }
  .contact__name {
    color: var(--gold);
    font-weight: 900;
    font-size: 15px;
    letter-spacing: 0.5px;
    text-transform: uppercase;
  }
  .contact__role { margin-bottom: 10px; }
  .contact__address { margin-bottom: 10px; }
  .contact__line { display: flex; align-items: center; gap: 7px; }
  .contact__icon { width: 12px; height: 12px; flex: none; }

  .card__pattern {
    position: absolute; inset: 0;
    background: linear-gradient(120deg, var(--card) 0%, var(--card-pattern) 60%, #353535 100%);
  }
  .card--back .brand {
    position: absolute; inset: 0;
    justify-content: center;
  }
</style>
</head>
<body>

  <section class="card card--front">
    <div class="brand">
      <div class="brand__name"><span class="brand__square"></span>HARBOURLINE</div>
      <div class="brand__sub">SUITES</div>
    </div>
    <div class="divider"></div>
    <div class="contact">
      <p class="contact__name">Marcus Elden</p>
      <p class="contact__role">Manager</p>
      <p class="contact__address">Your Address, City<br>State, Zip 0000</p>
      <p class="contact__line">
        <svg class="contact__icon" viewBox="0 0 12 12"><circle cx="6" cy="6" r="6" fill="var(--gold)"/><path d="M3.5 3.5 L5 3.5 L5.5 5 L4.8 5.6 Q5.6 7 6.6 7.4 L7.2 6.7 L8.6 7.2 L8.6 8.6 Q5 8.8 3.5 3.5Z" fill="var(--card)"/></svg>
        555-014-2200
      </p>
      <p class="contact__line">
        <svg class="contact__icon" viewBox="0 0 12 12"><rect x="0.5" y="2.5" width="11" height="7.5" fill="var(--gold)"/><path d="M0.5 2.5 L6 7 L11.5 2.5" fill="none" stroke="var(--card)" stroke-width="1"/></svg>
        marcus@harbourlinesuites.com
      </p>
      <p class="contact__line">
        <svg class="contact__icon" viewBox="0 0 12 12"><circle cx="6" cy="6" r="5.5" fill="var(--gold)"/><circle cx="6" cy="6" r="2.5" fill="none" stroke="var(--card)" stroke-width="1"/><path d="M0.5 6 H11.5 M6 0.5 V11.5" stroke="var(--card)" stroke-width="0.8"/></svg>
        www.harbourlinesuites.com
      </p>
    </div>
  </section>

  <section class="card card--back">
    <div class="card__pattern" role="img" aria-label="Embossed repeating brand pattern in dark tones"></div>
    <div class="brand">
      <div class="brand__name"><span class="brand__square"></span>HARBOURLINE</div>
      <div class="brand__sub">SUITES</div>
    </div>
  </section>

</body>
</html>
```